Bluestone Advisory & Mgmt - Professional Business Cards

Hi!

I am a Real Estate Developer and Construction Consultant.

I have a lot of inspiration from previous designs and would be open to using the attached Designs as a starting point. I would like to see these styles incorporated into your designs.

I really need professional business card to go with it that includes my important info.

Look forward to seeing your designs!.

Target Market(s)

My Target market are building owners, lawyers, consultants.

Industry/Entity Type

Real Estate Development

Contact Information for Business Card

My Name: Dorian Pelkey
My Title: Principle
Company Name: Bluestone Advisory & Mgmt, LLC
Address: 348 West 71st Street, 9th FL New York, NY 10010
Mobile: 917.806.3971
Website: bam-hvx.example

Font styles to use
Serif
Sans Serif

Colors

Designer to choose colors to be used in the design.

Requirements
Must have
• Must incorporate the logo attached or have new that looks similar.
• Must use professional font that will be seen and judged by wealthy land owners and developers.
• Must incorporate some of the color green.
Should not have
• Photo's or pictures of people or buildings of any kind.

```html
<!DOCTYPE html>
<html lang="en">
<head>
<meta charset="utf-8">
<title>Bluestone Advisory &amp; Mgmt – Business Cards</title>
<link rel="stylesheet" href="https://fonts.googleapis.com/css2?family=Open+Sans:wght@400;600;800&display=swap">
<style>
  :root {
    --bg: #e9e6e1;
    --paper: #f6f6f4;
    --green: #45a36e;
    --green-dark: #1f5a37;
    --stripe: #8e8786;
    --ink: #3d3d3d;
    --ink-soft: #555;
    --white: #ffffff;
  }
  * { margin: 0; padding: 0; box-sizing: border-box; }
  html, body {
    width: 1200px; height: 1200px; overflow: hidden;
    background: var(--bg);
    font-family: "Open Sans", Arial, sans-serif;
  }
  .card {
    position: absolute; left: 180px;
    width: 840px; height: 480px;
    overflow: hidden;
    box-shadow: 0 6px 18px rgba(0,0,0,.12);
  }
  .card--front { top: 100px; background: var(--paper); }
  .card--back { top: 630px; background: var(--green); }

  .card__wave { position: absolute; inset: 0; width: 100%; height: 100%; }

  .contact { position: absolute; left: 56px; top: 44px; color: var(--ink); }
  .contact__name { font-size: 38px; font-weight: 800; letter-spacing: .5px; }
  .contact__title { font-size: 22px; color: var(--ink-soft); margin-top: 2px; }
  .contact__list { list-style: none; margin-top: 28px; }
  .contact__item {
    display: flex; align-items: center; gap: 14px;
    font-size: 21px; line-height: 1.2; margin-bottom: 12px;
  }
  .contact__icon { width: 22px; height: 22px; flex: none; }
  .contact__address { font-size: 18px; line-height: 1.3; margin-left: 36px; color: var(--ink); }
  .contact__address .company { display: block; }

  .brand-name {
    position: absolute; font-weight: 800; letter-spacing: -1px;
  }
  .card--front .brand-name {
    right: 50px; top: 170px; font-size: 68px; color: var(--green);
  }
  .card--back .brand-name {
    left: 0; right: 0; top: 50%; transform: translateY(-50%);
    text-align: center; font-size: 110px; color: var(--white);
  }
</style>
</head>
<body>

<section class="card card--front" aria-label="Business card front">
  <svg class="card__wave" viewBox="0 0 840 480" preserveAspectRatio="none" aria-hidden="true">
    <path d="M0,330 C200,330 420,395 600,420 C720,436 800,425 840,400 L840,480 L0,480 Z" fill="var(--stripe)"/>
    <path d="M0,348 C200,348 420,413 600,438 C720,454 800,443 840,418 L840,480 L0,480 Z" fill="var(--green)"/>
  </svg>

  <div class="contact">
    <h1 class="contact__name">Dorian Pelkey</h1>
    <p class="contact__title">President</p>
    <ul class="contact__list">
      <li class="contact__item">
        <svg class="contact__icon" viewBox="0 0 24 24" fill="none" stroke="var(--ink)" stroke-width="1.6"><rect x="6" y="2" width="12" height="20" rx="2"/><line x1="10" y1="19" x2="14" y2="19"/></svg>
        917.806.3971
      </li>
      <li class="contact__item">
        <svg class="contact__icon" viewBox="0 0 24 24" fill="none" stroke="var(--ink)" stroke-width="1.8"><rect x="2" y="5" width="20" height="14"/><polyline points="2,5 12,13 22,5"/></svg>
        dorian@bam-hvx.example
      </li>
      <li class="contact__item">
        <svg class="contact__icon" viewBox="0 0 24 24" fill="none" stroke="var(--ink)" stroke-width="1.4"><circle cx="12" cy="12" r="9"/><ellipse cx="12" cy="12" rx="4" ry="9"/><line x1="3" y1="12" x2="21" y2="12"/></svg>
        www.bam-hvx.example
      </li>
      <li class="contact__item">
        <svg class="contact__icon" viewBox="0 0 24 24" fill="var(--ink)"><path d="M12 2a6 6 0 0 0-6 6c0 4.5 6 13 6 13s6-8.5 6-13a6 6 0 0 0-6-6zm0 8.5a2.5 2.5 0 1 1 0-5 2.5 2.5 0 0 1 0 5z"/></svg>
        <span></span>
      </li>
    </ul>
    <p class="contact__address" style="margin-top:-40px">
      <span class="company">Bluestone Advisory &amp; Mgmt, LLC</span>
      348 West 71st Street, 9th FL New York,<br>NY 10010
    </p>
  </div>

  <div class="brand-name">Bluestone</div>
</section>

<section class="card card--back" aria-label="Business card back">
  <div class="brand-name">Bluestone</div>
</section>

</body>
</html>
```